Corvin Staffing Partners Business Cards

Business cards with logo design for a new recruiting company called "Corvin Staffing Partners"

incorporate RED & BLUE colors

Final design should reflect strength - clean, elegant design

Company name superimposed upon graphic (Greek Columns)

Please see attached Photos!!!

Industry/Entity Type

Business

Font styles to use
Decorative

Colors
ec2027
0555a3
85cae6

Requirements
Must have
• Must look very similar to attached design!!!

Want Company name superimposed upon graphic (Greek Columns)

Tag line at bottom must be included:
"Empowering Exceptional Companies with Exceptional People"

```html
<!DOCTYPE html>
<html lang="en">
<head>
<meta charset="utf-8">
<title>Corvin Staffing Partners — Business Card</title>
<link rel="stylesheet" href="https://fonts.googleapis.com/css2?family=Questrial&family=Open+Sans:wght@700&display=swap">
<style>
  :root {
    --red: #ec2027;
    --blue: #0555a3;
    --sky: #85cae6;
    --ink: #3a3a3a;
    --paper: #ffffff;
    --backdrop: #e6e7e9;
    --stone-dark: #1c1c1c;
    --stone-light: #8a8a8a;
  }
  * { margin: 0; padding: 0; box-sizing: border-box; }
  html, body {
    width: 1200px; height: 1000px; overflow: hidden;
    background: var(--backdrop);
    font-family: "Questrial", sans-serif;
  }
  .card {
    position: absolute; left: 100px; top: 214px;
    width: 1000px; height: 572px;
    background: var(--paper);
    overflow: hidden;
    box-shadow: 0 6px 24px rgba(0,0,0,0.12);
  }
  .top-band {
    position: absolute; left: 0; top: 0; width: 100%; height: 16px;
    background: var(--sky);
  }
  .brand-square {
    position: absolute; left: 44px; top: 56px;
    width: 86px; height: 86px; background: var(--blue);
  }
  .columns-art {
    position: absolute; left: 160px; top: 46px;
    width: 240px; height: 240px;
  }
  .brand-name {
    position: absolute; left: 160px; top: 292px;
    color: var(--blue); font-size: 46px; line-height: 52px;
  }
  .divider {
    position: absolute; left: 520px; top: 110px;
    width: 4px; height: 320px; background: var(--red);
  }
  .person {
    position: absolute; left: 580px; top: 130px;
    color: var(--blue);
  }
  .person-name {
    font-family: "Open Sans", sans-serif; font-weight: 700;
    font-size: 30px;
  }
  .person-title { font-size: 26px; margin-top: 2px; }
  .contacts {
    position: absolute; left: 580px; top: 244px;
    list-style: none;
  }
  .contact {
    display: flex; align-items: center; gap: 22px;
    height: 60px; color: var(--ink); font-size: 26px;
  }
  .contact svg { width: 34px; height: 34px; flex: none; }
  .rule-dark {
    position: absolute; left: 0; top: 470px; width: 100%; height: 8px;
    background: var(--blue);
  }
  .tagline-band {
    position: absolute; left: 0; top: 478px; width: 100%; height: 94px;
    background: var(--sky);
    display: flex; align-items: center; justify-content: center;
  }
  .tagline { color: var(--paper); font-size: 30px; }
  .tagline .accent {
    color: var(--red); font-family: "Open Sans", sans-serif; font-weight: 700;
  }
</style>
</head>
<body>
  <article class="card">
    <div class="top-band"></div>

    <div class="brand-square"></div>
    <svg class="columns-art" viewBox="0 0 240 240" role="img" aria-label="Illustration of two classical Greek columns">
      <defs>
        <linearGradient id="stone" x1="0" y1="0" x2="1" y2="0">
          <stop offset="0" stop-color="var(--stone-dark)"/>
          <stop offset="0.5" stop-color="var(--stone-light)"/>
          <stop offset="1" stop-color="var(--stone-dark)"/>
        </linearGradient>
      </defs>
      <rect width="240" height="240" fill="url(#stone)" opacity="0.85"/>
    </svg>
    <div class="brand-name">Corvin<br>Staffing<br>Partners</div>

    <div class="divider"></div>

    <div class="person">
      <div class="person-name">Daniel R. Whitlock</div>
      <div class="person-title">President</div>
    </div>

    <ul class="contacts">
      <li class="contact">
        <svg viewBox="0 0 34 34" aria-hidden="true">
          <rect x="10" y="6" width="14" height="24" rx="2" fill="none" stroke="#555" stroke-width="2"/>
          <rect x="13" y="9" width="8" height="7" fill="#555"/>
          <line x1="12" y1="2" x2="12" y2="6" stroke="#555" stroke-width="2"/>
        </svg>
        512.555.0148
      </li>
      <li class="contact">
        <svg viewBox="0 0 34 34" aria-hidden="true">
          <rect x="3" y="8" width="28" height="19" fill="#555"/>
          <polyline points="3,8 17,19 31,8" fill="none" stroke="#fff" stroke-width="2"/>
        </svg>
        DWhitlock@CorvinSP.com
      </li>
      <li class="contact">
        <svg viewBox="0 0 34 34" aria-hidden="true">
          <circle cx="17" cy="17" r="13" fill="#666"/>
          <ellipse cx="17" cy="17" rx="6" ry="13" fill="none" stroke="#ccc" stroke-width="1.5"/>
          <line x1="4" y1="17" x2="30" y2="17" stroke="#ccc" stroke-width="1.5"/>
        </svg>
        www.CorvinSP.com
      </li>
    </ul>

    <div class="rule-dark"></div>
    <div class="tagline-band">
      <p class="tagline">Empowering Exceptional Companies with <span class="accent">Exceptional</span> People</p>
    </div>
  </article>
</body>
</html>
```